A new company focused on starting and investing in transformative businesses.

We need a simple and clean website with a few pages. we like larkmeadow.com as a starting point. we want the landing page to be very simple with an option to click through on the top right into INVESTOR LOGIN. then we want to be able to scroll down to see more about our company.

Target Market(s)

professional

Coding

Coded - Design and coding required

Number of Pages Required

2 page

Font styles to use
Serif
Sans Serif

Requirements
Must have
• HALVERN BUILDERS logo (attached as a file) on the top with INVESTOR LOGIN as a click through on the right. Please model the click through from larkmeadow.com. The description (also written in attached file) should be on the landing page. we do not want to have to scroll to read the description.

Then we can scroll down to read more about Halvern including the mission and the two types of businesses. More is detailed on the attached file called "Halvern Website Syntax"
Should not have
• should not be slow loading with lots of fancy graphics. should not be busy and with too many colors.

```html
<!DOCTYPE html>
<html lang="en">
<head>
<meta charset="utf-8">
<title>Halvern Builders</title>
<link href="https://fonts.googleapis.com/css2?family=Poppins:wght@300;400;500;600&display=swap" rel="stylesheet">
<style>
  :root {
    --brand-blue: #03579e;
    --brand-blue-light: #2f7fc4;
    --ribbon-light: #eef5fb;
    --ribbon-mid: #c6dcf0;
    --ink: #111418;
    --muted: #9a9ea4;
    --white: #ffffff;
  }
  * { margin: 0; padding: 0; box-sizing: border-box; }
  html, body { width: 768px; height: 1200px; overflow: hidden; background: var(--white); }
  body { font-family: "Poppins", Arial, sans-serif; color: var(--ink); position: relative; }

  .hero { position: absolute; left: 0; top: 0; width: 768px; height: 530px; overflow: hidden; }
  .ribbon-area {
    position: absolute; left: 20px; top: 90px; width: 748px; height: 400px;
    background: radial-gradient(ellipse at 45% 55%, var(--ribbon-mid) 0%, var(--ribbon-light) 55%, rgba(255,255,255,0) 75%);
  }
  .hero-photo {
    position: absolute; left: 548px; top: 150px; width: 128px; height: 170px;
    background: linear-gradient(150deg, #d9d2c8 0%, #b89478 45%, #7f8f9a 100%);
  }
  .brand { position: absolute; left: 66px; top: 40px; display: flex; align-items: center; gap: 8px; }
  .brand-mark { width: 22px; height: 22px; background: var(--brand-blue); }
  .brand-name { font-weight: 600; font-size: 12px; line-height: 1.15; color: var(--ink); letter-spacing: 0.02em; }
  .investor-login {
    position: absolute; left: 624px; top: 37px; width: 86px; height: 22px;
    border-radius: 11px; background: var(--brand-blue); color: var(--white);
    font-size: 7px; font-weight: 500; display: flex; align-items: center; justify-content: center;
    text-decoration: none;
  }
  .hero-title {
    position: absolute; left: 84px; top: 170px; width: 420px;
    font-size: 21px; font-weight: 500; line-height: 1.45; color: var(--ink);
  }
  .scroll-cue { position: absolute; left: 375px; top: 440px; }

  .about { position: absolute; left: 0; top: 530px; width: 768px; height: 440px; }
  .mission-card { position: absolute; left: 52px; top: 60px; width: 336px; height: 254px; }
  .mission-card svg { position: absolute; inset: 0; }
  .mission-content { position: absolute; inset: 0; padding: 48px 36px 0; text-align: center; color: var(--white); }
  .mission-title { font-size: 23px; font-weight: 500; display: inline-block; position: relative; padding-bottom: 6px; }
  .mission-title::after {
    content: ""; position: absolute; left: 0; bottom: 0; width: 80px; height: 2px; background: var(--brand-blue-light);
  }
  .mission-text { margin-top: 26px; font-size: 14.5px; line-height: 1.55; font-weight: 400; }

  .focus { position: absolute; left: 420px; top: 90px; width: 300px; }
  .focus-title {
    font-size: 20px; font-weight: 500; color: var(--brand-blue); display: inline-block; position: relative; padding-bottom: 2px;
  }
  .focus-title::after {
    content: ""; position: absolute; left: 0; bottom: 0; width: 66px; height: 1.5px; background: var(--brand-blue);
  }
  .focus-text { margin: 8px 0 12px; font-size: 10px; line-height: 1.55; color: var(--muted); font-weight: 300; }

  .site-footer {
    position: absolute; left: 0; top: 970px; width: 768px; height: 230px; background: var(--brand-blue); color: var(--white);
  }
  .footer-brand { position: absolute; left: 156px; top: 56px; display: flex; align-items: center; gap: 8px; }
  .footer-brand .brand-mark { width: 26px; height: 26px; background: var(--white); }
  .footer-brand .brand-name { color: var(--white); font-size: 14px; }
  .footer-contact { position: absolute; left: 490px; top: 48px; font-size: 12px; line-height: 1.5; font-weight: 500; }
  .footer-rule { position: absolute; left: 31px; top: 158px; width: 706px; height: 2px; background: var(--white); }
  .copyright { position: absolute; left: 0; top: 174px; width: 768px; text-align: center; font-size: 7.5px; font-weight: 400; }
</style>
</head>
<body>
  <header class="hero">
    <div class="ribbon-area" role="img" aria-label="Soft translucent blue flowing ribbon illustration sweeping across the hero"></div>
    <div class="hero-photo" role="img" aria-label="Photo of business people reviewing charts and documents at a desk"></div>

    <div class="brand">
      <span class="brand-mark"></span>
      <span class="brand-name">HALVERN<br>BUILDERS</span>
    </div>
    <a class="investor-login" href="#">Investor Login</a>

    <h1 class="hero-title">Halvern Builders is an entrepreneurial firm focused on building and growing transformational companies</h1>

    <svg class="scroll-cue" width="18" height="10" viewBox="0 0 18 10" aria-hidden="true">
      <path d="M1 1 L9 8 L17 1" fill="none" stroke="var(--brand-blue)" stroke-width="2"/>
    </svg>
  </header>

  <section class="about">
    <div class="mission-card">
      <svg viewBox="0 0 336 254" preserveAspectRatio="none" aria-hidden="true">
        <path d="M30 0 L280 10 C305 12 318 30 322 60 L336 200 C340 230 320 242 290 244 L26 252 C10 252 0 240 0 220 L0 40 C0 15 10 0 30 0 Z" fill="var(--brand-blue)"/>
      </svg>
      <div class="mission-content">
        <h2 class="mission-title">Our mission</h2>
        <p class="mission-text">Our mission is to build meaningful businesses that create enduring value by impacting people in a measurable way.</p>
      </div>
    </div>

    <div class="focus">
      <h3 class="focus-title">Ground Up</h3>
      <p class="focus-text">Our ground up business applies a proven analytic process to identify value edge, a form of competitive advantage. We architect transformational companies and are deliberate in creating the foundation necessary to lead an industry.</p>
      <h3 class="focus-title">Special Opportunities</h3>
      <p class="focus-text">We partner with exceptional teams that create value by transforming lives. Our investment focus includes large companies and spin-outs.</p>
    </div>
  </section>

  <footer class="site-footer">
    <div class="footer-brand">
      <span class="brand-mark"></span>
      <span class="brand-name">HALVERN<br>BUILDERS</span>
    </div>
    <p class="footer-contact">Halvern Builders<br>For media inquiries, please contact<br>press@halvernbuilders.com</p>
    <div class="footer-rule"></div>
    <p class="copyright">© 2020 all rights reserved</p>
  </footer>
</body>
</html>
```